Business card for a young woman who performs life enhancement activities with people who have developmental disabilities, what used to be called retardation. She wants to focus on the creative part of her work. She has a degree in art and will engage clients in art projects as well as helping them learn to do things like grocery shop, cook meals, set goals, and live independently.

Target Market(s)

Parents, caregivers, guardians, relatives of people with developmental disabilities, meaning they have not developed in their mental capacities.

Industry/Entity Type

Business

Contact Information for Business Card

Bright Path Care Studio, Marisa J. Tolliver, 417 263-9184, marisa@marisatolliver.example, Life enhancement services for people with developmental disabilities. No address.

Font styles to use
Serif

Requirements
Must have
• Marisa wants it to have some indication of the art or creative part of her work with clients. But it must also be businesslike so it appeals to the parents. They have to see her as a professional, but she's compassionate and artsy. She wants just her company name on the front. The other information should be on the back.

```html
<!DOCTYPE html>
<html lang="en">
<head>
<meta charset="utf-8">
<title>Bright Path Care Studio – Business Card</title>
<link href="https://fonts.googleapis.com/css2?family=Lora:wght@400;700&display=swap" rel="stylesheet">
<style>
  :root {
    --bg: #2b2b2d;
    --violet: #8a0ff0;
    --violet-deep: #7406d6;
    --lavender: #b79be6;
    --paper: #f4f4f6;
    --slate: #4f5a93;
    --white: #ffffff;
  }
  * { box-sizing: border-box; margin: 0; padding: 0; }
  html, body {
    width: 1200px; height: 997px; overflow: hidden;
    background: var(--bg);
    font-family: "Lora", Georgia, serif;
  }
  .stage { position: relative; width: 1200px; height: 997px; }

  .card {
    position: absolute;
    width: 520px; height: 300px;
    border-radius: 22px;
    overflow: hidden;
    background: linear-gradient(180deg, var(--violet) 0%, var(--violet-deep) 100%);
  }

  /* Front */
  .card--front { left: 110px; top: 120px; }
  .front-panel {
    position: absolute; left: 100px; top: 0; width: 330px; height: 100%;
    background: var(--paper);
  }
  .front-name {
    position: absolute; left: 126px; top: 88px; width: 290px;
    color: var(--slate); font-weight: 700; font-size: 34px; line-height: 1.15;
  }
  .front-ribbon {
    position: absolute; left: 82px; top: 218px; width: 348px; height: 46px;
    background: var(--lavender);
  }

  /* Back */
  .card--back { left: 570px; top: 520px; }
  .back-top {
    position: absolute; left: 0; top: 0; width: 360px; height: 112px;
    color: var(--white); text-align: center; padding-top: 24px;
  }
  .back-company { font-weight: 700; font-size: 23px; line-height: 1.2; }
  .back-tagline { font-weight: 700; font-size: 13px; line-height: 1.3; margin-top: 8px; }
  .back-name-band {
    position: absolute; left: 0; top: 112px; width: 360px; height: 78px;
    background: var(--paper);
  }
  .rule {
    position: absolute; left: 60px; width: 240px; height: 1.5px; background: var(--violet);
  }
  .rule--top { top: 8px; }
  .rule--bottom { top: 68px; }
  .flourish {
    position: absolute; left: 150px; width: 60px; height: 5px;
    border-radius: 3px; background: var(--violet);
  }
  .flourish--top { top: 13px; }
  .flourish--bottom { top: 59px; }
  .person-name {
    position: absolute; left: 0; top: 22px; width: 100%;
    text-align: center; color: var(--violet);
    font-weight: 700; font-size: 27px; line-height: 1.2;
  }
  .contact-list {
    position: absolute; left: 30px; top: 208px; list-style: none;
    color: var(--white); font-weight: 700; font-size: 15px;
  }
  .contact-list li { display: flex; align-items: center; height: 26px; white-space: nowrap; }
  .contact-list svg { width: 16px; height: 16px; margin-right: 18px; fill: var(--white); flex: none; }

  .artwork {
    position: absolute; left: 360px; width: 160px; height: 100px;
  }
  .artwork--watercolour { top: 0; background: radial-gradient(circle at 65% 40%, #e46aa8 0 28%, #a89cb0 60%, #8f8799 100%); }
  .artwork--sculpture { top: 100px; background: radial-gradient(circle at 50% 50%, #5d7e86 0 22%, #3e4044 60%, #2b2c2f 100%); }
  .artwork--figure { top: 200px; background: radial-gradient(circle at 50% 55%, #c9b49a 0 18%, #3f8aa3 32%, #1d1e20 70%); }
</style>
</head>
<body>
<main class="stage">

  <section class="card card--front" aria-label="Card front">
    <div class="front-panel"></div>
    <h1 class="front-name">Bright Path Care Studio</h1>
    <div class="front-ribbon"></div>
  </section>

  <section class="card card--back" aria-label="Card back">
    <header class="back-top">
      <h2 class="back-company">Bright Path Care Studio</h2>
      <p class="back-tagline">Life enhancement services<br>for people with developmental disabilities.</p>
    </header>

    <div class="back-name-band">
      <span class="rule rule--top"></span>
      <span class="flourish flourish--top" role="img" aria-label="Decorative flourish"></span>
      <p class="person-name">Marisa J. Tolliver</p>
      <span class="flourish flourish--bottom" role="img" aria-label="Decorative flourish"></span>
      <span class="rule rule--bottom"></span>
    </div>

    <ul class="contact-list">
      <li>
        <svg viewBox="0 0 16 16" aria-hidden="true"><path d="M2 5c0-2 2-3 6-3s6 1 6 3v1h-3V5H5v1H2zM4 7h8l2 6H2z"/></svg>
        417 263-9184
      </li>
      <li>
        <svg viewBox="0 0 16 16" aria-hidden="true"><path d="M1 3h14v10H1zM2.5 4.5v.4L8 9l5.5-4.1v-.4z"/></svg>
        marisa@marisatolliver.example
      </li>
      <li>
        <svg viewBox="0 0 16 16" aria-hidden="true"><path d="M8 1a7 7 0 1 0 0 14A7 7 0 0 0 8 1zm0 1.6a5.4 5.4 0 1 1 0 10.8A5.4 5.4 0 0 1 8 2.6zM7 4v5h4V7.6H8.4V4z"/></svg>
        www.marisatolliver.example
      </li>
    </ul>

    <div class="artwork artwork--watercolour" role="img" aria-label="Client artwork: watercolour of a pink vase with white flowers"></div>
    <div class="artwork artwork--sculpture" role="img" aria-label="Client artwork: teal metal sculpture"></div>
    <div class="artwork artwork--figure" role="img" aria-label="Client artwork: fabric figure with blue mosaic pattern"></div>
  </section>

</main>
</body>
</html>
```